Bref créative
RVM Ltd stationary set
letterhead, business cards, envelopes
I need single sided standard sized Business Card [3.5" x 2"]
Designer's choice
Professional
Martin K. Dobbs
Registered Patent Attorney
82 E. Parkhill Street
Suite 4785
Chicago, IL 60417
martindobbs@claimwisp.com
www.claimwisp.com
A version of the "old" letterhead can be downloaded here: https://claimwisp.filevault-example.net/shared/q8tr2m4vbnxwpla7c3dk
RVM logo (ai format)

```html
<!DOCTYPE html>
<html lang="en">
<head>
<meta charset="utf-8">
<title>RVM Ltd – Business Cards</title>
<link href="https://fonts.googleapis.com/css2?family=Arimo:wght@400;700&display=swap" rel="stylesheet">
<style>
  :root {
    --brand-blue: #1452ad;
    --card-white: #ffffff;
    --mark-grey: #6d6e71;
    --backdrop: #d9d9d9;
    --ink: #ffffff;
  }
  html, body {
    margin: 0;
    padding: 0;
    overflow: hidden;
  }
  body {
    width: 1200px;
    height: 851px;
    background: var(--backdrop);
    position: relative;
    font-family: "Arimo", Arial, sans-serif;
  }
  .card {
    position: absolute;
    box-sizing: border-box;
    box-shadow: 0 6px 14px rgba(0,0,0,0.25);
  }
  /* Front of card */
  .card-front {
    left: 408px; top: 108px;
    width: 444px; height: 264px;
    background: var(--card-white);
    padding: 12px;
  }
  .card-front .face {
    position: relative;
    width: 100%; height: 100%;
    background: var(--brand-blue);
    clip-path: polygon(0 0, 100% 0, 100% 88%, 94% 100%, 0 100%);
  }
  .front-brand {
    position: absolute;
    left: 50px; top: 72px;
    display: flex; align-items: center; gap: 10px;
  }
  .brand-square {
    width: 26px; height: 26px;
    background: var(--card-white);
  }
  .brand-name {
    font-weight: 700;
    font-size: 24px;
    color: var(--ink);
    letter-spacing: 1px;
  }
  .front-details {
    position: absolute;
    left: 215px; top: 22px;
    color: var(--ink);
    font-size: 11.5px;
    line-height: 1.35;
  }
  .holder-name { font-weight: 700; font-size: 14px; }
  .holder-title { font-size: 14px; margin-bottom: 22px; }
  .contact-block p { margin: 0; }
  .address { margin-bottom: 10px !important; }
  /* Backs of card */
  .card-back {
    top: 408px;
    width: 418px; height: 252px;
    display: flex; flex-direction: column; align-items: center;
  }
  .card-back-blue { left: 151px; background: var(--brand-blue); }
  .card-back-white { left: 610px; background: var(--card-white); }
  .back-brand {
    margin-top: 96px;
    display: flex; align-items: center; gap: 12px;
  }
  .back-brand .brand-square { width: 34px; height: 34px; }
  .back-brand .brand-name { font-size: 32px; }
  .card-back-white .brand-square { background: var(--brand-blue); }
  .card-back-white .brand-name { color: var(--mark-grey); }
  .web {
    position: absolute;
    bottom: 22px;
    font-size: 12px;
    letter-spacing: 0.5px;
    color: var(--ink);
  }
  .card-back-white .web { color: var(--brand-blue); }
</style>
</head>
<body>
  <section class="card card-front">
    <div class="face">
      <div class="front-brand">
        <span class="brand-square"></span>
        <span class="brand-name">RVM Ltd</span>
      </div>
      <div class="front-details">
        <div class="holder-name">Martin K. Dobbs</div>
        <div class="holder-title">Registered Patent Attorney</div>
        <div class="contact-block">
          <p>82 E. Parkhill Street, Suite 4785</p>
          <p class="address">Chicago, IL 60417</p>
          <p>Phone : 3125550143</p>
          <p>Cell : 3125550178</p>
          <p>Fax : 3125550192</p>
          <p>E-mail : martindobbs@claimwisp.com</p>
          <p>Web : www.claimwisp.com</p>
        </div>
      </div>
    </div>
  </section>

  <section class="card card-back card-back-blue">
    <div class="back-brand">
      <span class="brand-square"></span>
      <span class="brand-name">RVM</span>
    </div>
    <div class="web">www.claimwisp.com</div>
  </section>

  <section class="card card-back card-back-white">
    <div class="back-brand">
      <span class="brand-square"></span>
      <span class="brand-name">RVM</span>
    </div>
    <div class="web">www.claimwisp.com</div>
  </section>
</body>
</html>
```